Calloway Brothers Civil Construction website design

We want a Bold website to promote our Heavy Civil Construction company, We would like an organic / tangible feel to the site. The pictures will be over saturated so they pop. We need to be able to easliy upload new projects and pictures on a regular basis.
Home page will have a full screen width image, "home page image" with silhouette and logo. It will also have about us area and picture
Page 2 will be Project Gallery with pictures in project folders
Page 3 will be an employment application form and submission
Page 4 will be Contact Us
Construction indusrty
Contractor
Coded - Design and coding required
4 page
- Hypatia Sans Pro Light

```html
<!DOCTYPE html>
<html lang="en">
<head>
<meta charset="utf-8">
<title>Calloway Brothers Civil Construction</title>
<link href="https://fonts.googleapis.com/css2?family=Roboto:wght@400;500;700&family=Lato:wght@400;700&display=swap" rel="stylesheet">
<style>
:root{
  --teal:#1b9fb8;
  --sky:#2fa3e0;
  --indigo:#3a4aa0;
  --slate:#414d5e;
  --slate-deep:#2f3945;
  --ink:#2b2b2b;
  --grey:#777c82;
  --white:#ffffff;
}
*{margin:0;padding:0;box-sizing:border-box}
html,body{width:1200px;height:2727px;overflow:hidden;background:var(--white)}
body{position:relative;font-family:"Roboto",Arial,sans-serif;color:var(--ink)}
.abs{position:absolute}
.topbar{left:0;top:0;width:1200px;height:32px}
.social{right:52px;top:10px;display:flex;gap:8px}
.social span{width:10px;height:10px;border-radius:50%;background:var(--white);display:block}
.brand{left:183px;top:48px;font-family:"Lato",sans-serif;font-weight:400;font-size:13px;color:var(--indigo);display:flex;align-items:center;gap:8px;white-space:nowrap}
.brand-mark{width:22px;height:22px;border:2px solid var(--indigo)}
.info{top:51px;display:flex;gap:10px;font-family:"Lato",sans-serif;font-size:11px;line-height:16px;color:var(--sky)}
.info em{font-style:normal;color:var(--grey);display:block}
.nav{left:0;top:100px;width:1200px;height:31px;background:var(--sky);display:flex;justify-content:center;align-items:center;gap:16px;font-family:"Lato",sans-serif;font-size:12px;letter-spacing:1.4px;color:var(--white)}
.hero{left:191px;top:180px;width:818px;height:490px;background:linear-gradient(180deg,#3a3f96 0%,#4b5bb0 45%,#5a6cb8 70%,#1a1a2a 92%,#111 100%);display:flex;align-items:center;justify-content:center}
.hero-name{font-family:"Lato",sans-serif;font-weight:400;font-size:28px;color:#151515;text-align:center}
.h2{font-weight:500;color:var(--teal);text-align:center}
.lead{font-weight:700;font-size:14.5px;line-height:18px;text-align:center;color:var(--ink)}
.svc{top:916px;width:152px}
.svc-icon{height:74px;border:2px solid var(--teal);border-radius:37px;display:flex;align-items:center;justify-content:center}
.svc h3{margin-top:42px;font-weight:500;font-size:27px;line-height:27px;color:var(--teal);text-align:center;height:132px}
.svc p{font-weight:500;font-size:12px;line-height:19px;color:var(--grey);text-align:center}
.box{border:2px solid var(--teal);border-radius:3px;height:74px;display:flex;align-items:center;justify-content:center}
.box-title{font-weight:500;font-size:23.5px;line-height:25px;color:var(--teal)}
.values{left:180px;top:2196px;width:830px;list-style:none;font-weight:500;font-size:11.5px;line-height:18px;color:#555}
.values li{position:relative;padding-left:12px;margin-bottom:15px}
.values li::before{content:"";position:absolute;left:0;top:6px;width:5px;height:5px;border:1px solid #888;border-radius:50%}
.footer{left:0;top:2435px;width:1200px;height:254px;background:var(--slate)}
.foot-h{font-family:"Lato",sans-serif;font-size:23px;color:var(--sky);letter-spacing:1px;border-bottom:2px solid var(--sky);width:405px;padding-bottom:6px}
.foot-menu{left:183px;top:2512px;list-style:none;font-family:"Lato",sans-serif;font-size:13px;color:var(--white);line-height:26.5px}
.search-field{left:611px;top:2511px;width:405px;height:30px;border-radius:15px;background:var(--white);font-family:"Lato",sans-serif;font-size:11px;color:#888;display:flex;align-items:center;justify-content:center}
.search-btn{left:611px;top:2546px;width:45px;height:32px;border-radius:16px;background:var(--sky);color:var(--white);font-size:8px;display:flex;align-items:center;justify-content:center}
.copyright{left:0;top:2689px;width:1200px;height:38px;background:var(--slate-deep);color:var(--white);font-family:"Lato",sans-serif;font-weight:700;font-size:10.5px;display:flex;align-items:center;justify-content:center}
</style>
</head>
<body>

<svg class="abs topbar" width="1200" height="32" viewBox="0 0 1200 32">
  <path d="M600 0 H1200 V32 H650 C630 32 625 0 600 0 Z" fill="var(--slate)"/>
</svg>
<div class="abs social"><span></span><span></span></div>

<div class="abs brand">
  <div class="brand-mark"></div>
  <span>Calloway Brothers Civil Construction</span>
</div>

<div class="abs info" style="left:466px">
  <svg width="20" height="26" viewBox="0 0 20 26"><path d="M10 1a8 8 0 0 0-8 8c0 6 8 15 8 15s8-9 8-15a8 8 0 0 0-8-8z" fill="var(--sky)"/><circle cx="10" cy="9" r="3" fill="#fff"/></svg>
  <div>Harbor Lane<em>Westfield</em></div>
</div>
<div class="abs info" style="left:651px">
  <svg width="26" height="26" viewBox="0 0 26 26"><circle cx="13" cy="14" r="10" fill="none" stroke="var(--sky)" stroke-width="3"/><path d="M13 8v6h5" stroke="var(--sky)" stroke-width="2" fill="none"/></svg>
  <div>08 : 14<em>Mon-Fri</em></div>
</div>
<div class="abs info" style="left:833px">
  <svg width="24" height="24" viewBox="0 0 24 24"><path d="M5 2l4 4-2 3c1 3 4 6 7 7l3-2 4 4-3 4C10 22 2 14 2 5z" fill="#555"/></svg>
  <div>555-014-2200<em>555-014-2201</em></div>
</div>

<nav class="abs nav"><span>HOME</span><span>PROJECT GALLERY</span><span>CARRERS</span><span>CONTACT US</span></nav>

<div class="abs hero" role="img" aria-label="Dusk sky over silhouetted excavators and heavy machinery">
  <div class="hero-name">Calloway Brothers Civil Construction</div>
</div>

<h2 class="abs h2" style="left:0;top:734px;width:1200px;font-size:23.5px">Our services</h2>
<p class="abs lead" style="left:190px;top:795px;width:820px">Many years of experience, professional employees and complete machinery necessary for quality work execution, and business philosophy is based on the quality and conscientious performance of all works.</p>

<div class="abs svc" style="left:191px">
  <div class="svc-icon"><svg width="62" height="42" viewBox="0 0 62 42"><path d="M16 0h30l16 42H0z" fill="var(--teal)"/><rect x="28" y="6" width="6" height="8" fill="#fff"/><rect x="28" y="22" width="6" height="10" fill="#fff"/></svg></div>
  <h3>Roads and outdoor facilities</h3>
  <p>Works on infrastructure and finishing of road or pedestrian reconstruction</p>
</div>
<div class="abs svc" style="left:358px">
  <div class="svc-icon"><svg width="62" height="40" viewBox="0 0 62 40"><g fill="none" stroke="var(--teal)" stroke-width="5" stroke-linecap="round"><path d="M3 6q7-6 14 0t14 0 14 0 14 0"/><path d="M3 20q7-6 14 0t14 0 14 0 14 0"/><path d="M3 34q7-6 14 0t14 0 14 0 14 0"/></g></svg></div>
  <h3>Watercours e regulation</h3>
  <p style="margin-top:6px">Editing watercourses and changing water quantities that pass through watercourses</p>
</div>
<div class="abs svc" style="left:525px">
  <div class="svc-icon"><svg width="66" height="52" viewBox="0 0 66 52"><path d="M33 0l33 52H0z" fill="var(--teal)"/><path d="M33 8l7 11-7-3-7 3z" fill="#fff"/></svg></div>
  <h3>Rehabilitati on landslides</h3>
  <p>Very complex works that require maximum cautiousness, experience and knowledge</p>
</div>
<div class="abs svc" style="left:691px">
  <div class="svc-icon"><svg width="66" height="54" viewBox="0 0 66 54"><path d="M14 20a24 18 0 0 1 48-6z" fill="var(--teal)"/><path d="M36 16l-10 30" stroke="var(--teal)" stroke-width="4"/><rect x="4" y="46" width="40" height="5" fill="var(--teal)"/></svg></div>
  <h3>Arranging the coast</h3>
  <p>Arranging the coast, arranging the beaches, making the lake and putting them into operation</p>
</div>
<div class="abs svc" style="left:857px">
  <div class="svc-icon"><svg width="64" height="54" viewBox="0 0 64 54"><path d="M4 46c10-2 14-8 20-18S40 10 58 6" fill="none" stroke="var(--teal)" stroke-width="9" stroke-linecap="round"/><path d="M4 46c10-2 14-8 20-18S40 10 58 6" fill="none" stroke="#fff" stroke-width="2"/></svg></div>
  <h3>Water supply and sewerage</h3>
  <p>Construction, reconstruction and rehabilitation in the field of hydrotechnics</p>
</div>

<p class="abs lead" style="left:190px;top:1325px;width:820px">Calloway Brothers, as a contractor with international experience, constantly adapts its business activities to the market requirements, following the principles of corporate social responsibility and sustainable development.</p>

<div class="abs box" style="left:457px;top:1497px;width:277px">
  <svg width="40" height="54" viewBox="0 0 40 54"><path d="M2 2h36v6L24 27l14 19v6H2v-6l14-19L2 8z" fill="var(--teal)"/><path d="M8 46l12-14 12 14z" fill="#fff"/></svg>
</div>
<div class="abs box-title" style="left:457px;top:1586px;width:277px;text-align:center">Expect the terms</div>

<div class="abs box" style="left:192px;top:1696px;width:262px">
  <svg width="54" height="42" viewBox="0 0 54 42"><path d="M3 2v36h49" fill="none" stroke="var(--teal)" stroke-width="5"/><path d="M10 30l10-10 8 8 14-14" fill="none" stroke="var(--teal)" stroke-width="5"/><path d="M38 8h10v10z" fill="var(--teal)"/></svg>
</div>
<div class="abs box-title" style="left:192px;top:1785px;width:262px;text-align:center">Business development</div>

<div class="abs" style="left:454px;top:1740px;width:292px;text-align:center;font-weight:500;font-size:23.5px;color:#555">Mision of our Bussines</div>

<div class="abs box" style="left:747px;top:1696px;width:262px">
  <svg width="68" height="56" viewBox="0 0 68 56"><circle cx="24" cy="30" r="16" fill="none" stroke="var(--teal)" stroke-width="9" stroke-dasharray="6 4"/><circle cx="24" cy="30" r="8" fill="var(--teal)"/><circle cx="24" cy="30" r="4" fill="#fff"/><circle cx="54" cy="12" r="8" fill="var(--teal)"/><circle cx="54" cy="12" r="3" fill="#fff"/><circle cx="54" cy="44" r="8" fill="var(--teal)"/><circle cx="54" cy="44" r="3" fill="#fff"/></svg>
</div>
<div class="abs box-title" style="left:747px;top:1785px;width:262px;text-align:center">Constant business processes</div>

<div class="abs box" style="left:462px;top:1918px;width:276px">
  <svg width="68" height="40" viewBox="0 0 68 40"><path d="M2 8h12l10-4 12 4 10-4h8l12 4v18l-8 2-16 10-10 2-16-10-14-2z" fill="var(--teal)"/><path d="M24 14l8-4 14 12-6 4zM14 24l8 6" stroke="#fff" stroke-width="3" fill="none"/></svg>
</div>
<div class="abs box-title" style="left:462px;top:2008px;width:260px">Relationship with the client</div>

<ul class="abs values">
  <li>Fair and fair business towards all stakeholders is the foundation of our many years of success. We pay special attention to cooperation with our subcontractors and suppliers whose business depends directly on fulfilling our obligations towards them. We also respect copyright and related rights in all segments of our business, providing licenses or other forms of remuneration for using them.</li>
  <li>Working on the highest ethical principles in each of our business contacts gives us the freedom to always be proud of our business and maintain the outstanding reputation of our company.</li>
  <li>We are looking for new challenges, to learn and to progress as individuals and as an organization. This is accomplished through: timely identification of needs and possibilities of training and their realization, creating a positive and motivating environment for leadership and development and the introduction of modern business standards and practices.</li>
</ul>

<footer class="abs footer">
  <div class="abs foot-h" style="left:183px;top:22px">Menu</div>
  <div class="abs foot-h" style="left:611px;top:22px">Search</div>
</footer>
<ul class="abs foot-menu">
  <li>HOME</li><li>OUR SERVICES</li><li>Mision of our Bussines</li><li>PROJECT GALLERY</li><li>CARRERS</li><li>CONTACT US</li>
</ul>
<div class="abs search-field">Search</div>
<div class="abs search-btn">Search</div>
<div class="abs copyright">© Calloway Brothers Civil Construction 2019.</div>

</body>
</html>
```